Real Estate Webpage Design

We have an existing website: brindlewoodhomes.com.au
We focus customised service mainly on Property Management and second-hand property sales.
We are not entirely happy about the current design and layout can stay roughly the same as the back end coding is linked to a CRM system.
We would like to see the design are more reachable to our clients and appearing.
Please check our Website Design Draft for more details.

Industry/Entity Type

Real estate Agency

Number of Pages Required

5+ page

Font styles to use
Sans Serif

Colors

Designer to choose colors to be used in the design.

```html
<!DOCTYPE html>
<html lang="en">
<head>
<meta charset="utf-8">
<title>Brindlewood Homes – Real Estate</title>
<link href="https://fonts.googleapis.com/css2?family=Poppins:wght@300;400;500;600;700&display=swap" rel="stylesheet">
<style>
:root{
  --orange:#fdb42f;
  --orange-dark:#f2a516;
  --navy:#152540;
  --ink:#1d2433;
  --muted:#8a8f99;
  --cream:#fbedcc;
  --light:#f6f8fc;
  --white:#ffffff;
}
*{margin:0;padding:0;box-sizing:border-box}
html,body{width:1200px;height:4728px;overflow:hidden}
body{font-family:'Poppins',sans-serif;color:var(--ink);background:var(--white);position:relative}
.abs{position:absolute}
.btn{position:absolute;display:flex;align-items:center;justify-content:center;font-weight:600;font-size:13px;letter-spacing:.3px}
.btn-orange{background:var(--orange);color:var(--ink)}
.btn-white{background:var(--white);color:var(--ink)}
.btn-small{background:var(--orange);color:var(--white);font-weight:400;font-size:13px;border-bottom:3px solid #c9861a}

/* header + hero */
.hero{top:0;left:0;width:1200px;height:675px;background:linear-gradient(180deg,#4a5c6e 0%,#6e7d88 40%,#55606a 70%,#4c6a3e 100%)}
.hero-shade{top:0;left:0;width:1200px;height:675px;background:linear-gradient(90deg,rgba(18,28,40,.55),rgba(18,28,40,.1))}
.brand{top:14px;left:60px;display:flex;align-items:center;gap:12px}
.brand-mark{width:56px;height:56px;border-radius:50%;background:var(--orange)}
.brand-name{font-size:38px;font-weight:600;color:var(--orange);line-height:1}
.brand-sub{font-size:13px;color:var(--white);font-weight:500}
.nav{top:25px;left:435px;display:flex;gap:0}
.nav a{position:absolute;color:var(--white);font-size:13px;text-decoration:none;white-space:nowrap}
.nav a.active{color:var(--orange)}
.nav-underline{top:57px;left:433px;width:46px;height:2px;background:var(--orange)}
.add-btn{top:18px;left:1013px;width:127px;height:35px;font-weight:500;font-size:13px}
.hero-title{top:210px;left:60px;font-size:64px;font-weight:700;color:var(--white);line-height:68px}
.hero-text{top:352px;left:60px;width:620px;font-size:13px;color:var(--white);line-height:22px}
.hero-btn{top:435px;left:60px;width:322px;height:46px}

/* services */
.photo{background:linear-gradient(135deg,#6b6355,#a89a84 45%,#4d4a47)}
.service-panel{background:var(--orange)}
.service-title{font-size:36px;font-weight:600;line-height:46px;color:var(--ink)}
.service-text{font-size:13px;line-height:22.5px;color:var(--white)}

/* listings */
.listings{top:1820px;left:0;width:1200px;height:778px;background:var(--light)}
.section-title{position:absolute;left:0;width:1200px;text-align:center;font-size:34px;font-weight:500;color:var(--ink)}
.tabs{top:1932px;left:334px;display:flex}
.tab{width:106px;height:39px;border:1px solid #c9cdd4;display:flex;align-items:center;justify-content:center;font-size:13px;background:var(--white);margin-left:-1px}
.tab.active{background:var(--orange);color:var(--white);border-color:var(--orange)}
.card{top:2002px;width:340px;height:416px;background:var(--white);box-shadow:0 2px 10px rgba(0,0,0,.08)}
.card-img{position:absolute;top:11px;left:9px;width:322px;height:180px;background:linear-gradient(160deg,#8fb6e0,#cfd9e3 45%,#6b7d5f)}
.badge{position:absolute;top:0;left:0;background:var(--navy);color:var(--white);font-size:12px;padding:4px 8px}
.star{position:absolute;top:20px;right:20px}
.card-next{position:absolute;top:164px;right:22px;width:26px;height:26px;border-radius:50%;background:rgba(20,30,40,.55)}
.card-town{position:absolute;top:202px;left:20px;font-size:17px;font-weight:500}
.card-addr{position:absolute;top:235px;left:20px;font-size:13px;display:flex;gap:6px;align-items:center}
.card-meta{position:absolute;top:264px;left:20px;display:flex;gap:18px;font-size:13px;align-items:center}
.card-meta span{display:flex;align-items:center;gap:8px}
.card-insp{position:absolute;top:306px;left:20px;font-size:16px;font-weight:500}
.card-time{position:absolute;top:334px;left:20px;font-size:13px;color:var(--orange)}
.card-rule{position:absolute;top:364px;left:0;width:340px;height:1px;background:#e5e7eb}
.card-price{position:absolute;top:380px;left:22px;font-size:16px;font-weight:600}
.arrow-box{width:30px;height:30px;display:flex;align-items:center;justify-content:center}
.arrow-fill{background:var(--orange)}
.arrow-line{background:var(--white);border:1px solid var(--orange)}

/* about */
.about-photo{top:2598px;left:0;width:1200px;height:595px;background:linear-gradient(180deg,#b9c3c9,#9aa69c 45%,#54654a 80%,#3f4f3c)}
.about-panel{top:2958px;left:60px;width:1080px;height:431px;background:var(--cream);text-align:center}
.about-panel h2{margin-top:46px;font-size:34px;font-weight:600}
.about-panel p{width:640px;margin:14px auto 0;font-size:13px;line-height:22.5px;color:var(--muted)}
.about-panel p.note{width:760px;color:var(--orange)}

/* testimonial */
.quote-text{top:3566px;left:340px;width:520px;text-align:center;font-size:13px;line-height:22.5px;color:var(--muted)}
.quote-name{top:3726px;left:0;width:1200px;text-align:center;font-size:13px;font-weight:500}

/* contact */
.contact{top:3840px;left:0;width:1200px;height:558px;background:var(--navy)}
.contact-title{color:var(--white)}
.contact-text{top:3962px;left:290px;width:620px;text-align:center;color:var(--white);font-size:13px;line-height:22px}
.field{border-bottom:1px solid #3b4a63;color:#8fa3c4;font-size:13px;padding-bottom:10px}
.submit{top:4275px;left:495px;width:219px;height:43px}

/* footer */
.footer-text{font-size:12px;line-height:22px;color:var(--ink)}
.footer-head{font-size:13px;color:var(--orange);font-weight:500}
.footer-links a{display:block;color:var(--ink);text-decoration:none;font-size:12px;line-height:26.6px}
.social{width:35px;height:35px;border-radius:50%;border:1.5px solid var(--ink)}
.social.on{background:var(--orange);border-color:var(--orange)}
.copy-rule{top:4688px;left:0;width:1200px;height:1px;background:#e3e5ea}
.copy{top:4700px;font-size:12px;color:var(--ink)}
</style>
</head>
<body>

<!-- Hero -->
<div class="abs hero photo" role="img" aria-label="Modern two-storey concrete home with glazed ground floor at dusk"></div>
<div class="abs hero-shade"></div>
<div class="abs brand">
  <div class="brand-mark"></div>
  <div>
    <div class="brand-name">Brindlewood</div>
    <div class="brand-sub">Homes</div>
  </div>
</div>
<nav class="abs nav">
  <a class="active" style="left:0">Home</a>
  <a style="left:70px">About Us</a>
  <a style="left:152px">Leasing</a>
  <a style="left:229px">Buy</a>
  <a style="left:282px">Sell</a>
  <a style="left:330px">Our Team</a>
  <a style="left:422px">Blog</a>
  <a style="left:477px">Contact Us</a>
</nav>
<div class="abs nav-underline"></div>
<div class="btn btn-orange add-btn">Add Properties</div>
<h1 class="abs hero-title">Find your dream<br>home with Brindlewood</h1>
<p class="abs hero-text">Lorem Ipsum is simply dummy text of the printing and typesetting industry. Lorem Ipsum has been the industry's standard dummy text ever since the 1500s, when an unknown printer</p>
<div class="btn btn-orange hero-btn">MAKE LEASING YOUR PROPERTY HAPPEN</div>

<!-- Property Management -->
<div class="abs photo" style="top:807px;left:60px;width:690px;height:450px;background:linear-gradient(120deg,#3b3f46,#8c8478 50%,#2e3036)" role="img" aria-label="Agents in suits discussing a document with a client"></div>
<div class="abs service-panel" style="top:807px;left:750px;width:390px;height:450px"></div>
<h2 class="abs service-title" style="top:846px;left:796px">Property<br>Management</h2>
<p class="abs service-text" style="top:964px;left:796px;width:310px">Lorem Ipsum is simply dummy text of the printing and typesetting industry. Lorem Ipsum has been the industry's standard dummy text ever since the 1500s, when an unknown printer took a galley of type and scrambled it to make a type specimen book.</p>
<div class="btn btn-white" style="top:1132px;left:796px;width:158px;height:48px">THE APPRAISAL</div>

<!-- Property Sales -->
<div class="abs service-panel" style="top:1279px;left:60px;width:390px;height:451px"></div>
<div class="abs photo" style="top:1279px;left:450px;width:675px;height:451px;background:linear-gradient(160deg,#a9c7e6,#dfe6ea 45%,#3fa9b3 75%,#3d6a35)" role="img" aria-label="White modern villa with pool and palm trees"></div>
<h2 class="abs service-title" style="top:1355px;left:106px">Property sales</h2>
<p class="abs service-text" style="top:1428px;left:106px;width:300px">Lorem ipsum is simply dummy text of the printing and typesetting industry. Lorem Ipsum has been the industry's standard dummy text ever since the 1500s, when an unknown printer took a galley of type and scrambled it to make a type specimen book.</p>
<div class="btn btn-white" style="top:1596px;left:106px;width:158px;height:48px">THE APPRAISAL</div>

<!-- Listings -->
<div class="abs listings"></div>
<h2 class="section-title" style="top:1864px">Listings Available For Latest Property</h2>
<div class="abs tabs">
  <div class="tab active">For Sale</div>
  <div class="tab">For Lease</div>
  <div class="tab">Open Times</div>
  <div class="tab">Sold</div>
  <div class="tab">Leased</div>
</div>

<div class="abs arrow-box arrow-fill" style="top:2224px;left:15px"><svg width="10" height="14"><path d="M8 1L2 7l6 6" fill="none" stroke="#fff" stroke-width="1.6"/></svg></div>
<div class="abs arrow-box arrow-line" style="top:2224px;left:1154px"><svg width="10" height="14"><path d="M2 1l6 6-6 6" fill="none" stroke="#1d2433" stroke-width="1.6"/></svg></div>

<div class="abs card" style="left:60px">
  <div class="card-img" role="img" aria-label="Apartment tower with balconies and trees"></div>
  <div class="badge">On Sale</div>
  <svg class="star" width="20" height="20" viewBox="0 0 24 24"><path d="M12 2l3 7h7l-5.5 4.5 2 7.5L12 17l-6.5 4 2-7.5L2 9h7z" fill="#fdb42f"/></svg>
  <div class="card-next"></div>
  <div class="card-town">Harlow Park</div>
  <div class="card-addr"><svg width="12" height="16" viewBox="0 0 12 16"><path d="M6 15S1 9 1 6a5 5 0 0110 0c0 3-5 9-5 9z" fill="none" stroke="#fdb42f"/></svg>112/40 Heron Street Marlow Vale...</div>
  <div class="card-meta">
    <span><svg width="22" height="14"><rect x="1" y="4" width="20" height="9" fill="none" stroke="#fdb42f"/></svg>1</span>
    <span><svg width="22" height="14"><path d="M1 8h20v5H1zM5 8V2" fill="none" stroke="#fdb42f"/></svg>1</span>
    <span><svg width="26" height="14"><path d="M2 12V8l4-5h12l5 5v4z" fill="none" stroke="#fdb42f"/></svg>1</span>
  </div>
  <div class="card-insp">Next Inspection:</div>
  <div class="card-time">Sat 21st May 9:40 Am–10:00 Am</div>
  <div class="card-rule"></div>
  <div class="card-price">$369,900+</div>
</div>

<div class="abs card" style="left:428px">
  <div class="card-img" style="background:linear-gradient(160deg,#9dc4ea,#dfe9f2 45%,#2f8fb0 75%,#6a5b4c)" role="img" aria-label="High-rise with rooftop infinity pool"></div>
  <div class="badge">On Sale</div>
  <svg class="star" width="20" height="20" viewBox="0 0 24 24"><path d="M12 2l3 7h7l-5.5 4.5 2 7.5L12 17l-6.5 4 2-7.5L2 9h7z" fill="#fdb42f"/></svg>
  <div class="card-next"></div>
  <div class="card-town">Harlow Park</div>
  <div class="card-addr"><svg width="12" height="16" viewBox="0 0 12 16"><path d="M6 15S1 9 1 6a5 5 0 0110 0c0 3-5 9-5 9z" fill="none" stroke="#fdb42f"/></svg>Level 3/18/4 Wattlebird Avenue...</div>
  <div class="card-meta">
    <span><svg width="22" height="14"><rect x="1" y="4" width="20" height="9" fill="none" stroke="#fdb42f"/></svg>2</span>
    <span><svg width="22" height="14"><path d="M1 8h20v5H1zM5 8V2" fill="none" stroke="#fdb42f"/></svg>2</span>
    <span><svg width="26" height="14"><path d="M2 12V8l4-5h12l5 5v4z" fill="none" stroke="#fdb42f"/></svg>1</span>
  </div>
  <div class="card-insp">Next Inspection:</div>
  <div class="card-time">Sat 21st May 9:40 Am–10:00 Am</div>
  <div class="card-rule"></div>
  <div class="card-price">$5,00,000+</div>
</div>

<div class="abs card" style="left:800px">
  <div class="card-img" style="background:linear-gradient(160deg,#6a8fd0,#c8a7b8 40%,#8a8e92 70%,#3c4a3a)" role="img" aria-label="Suburban two-storey house with double garage"></div>
  <div class="badge">On Sale</div>
  <svg class="star" width="20" height="20" viewBox="0 0 24 24"><path d="M12 2l3 7h7l-5.5 4.5 2 7.5L12 17l-6.5 4 2-7.5L2 9h7z" fill="#fdb42f"/></svg>
  <div class="card-next"></div>
  <div class="card-town">Harlow Park</div>
  <div class="card-addr"><svg width="12" height="16" viewBox="0 0 12 16"><path d="M6 15S1 9 1 6a5 5 0 0110 0c0 3-5 9-5 9z" fill="none" stroke="#fdb42f"/></svg>Level 3/18/4 Wattlebird Avenue...</div>
  <div class="card-meta">
    <span><svg width="22" height="14"><rect x="1" y="4" width="20" height="9" fill="none" stroke="#fdb42f"/></svg>2</span>
    <span><svg width="22" height="14"><path d="M1 8h20v5H1zM5 8V2" fill="none" stroke="#fdb42f"/></svg>2</span>
    <span><svg width="26" height="14"><path d="M2 12V8l4-5h12l5 5v4z" fill="none" stroke="#fdb42f"/></svg>1</span>
  </div>
  <div class="card-insp">Next Inspection:</div>
  <div class="card-time">Sat 21st May 9:40 Am–10:00 Am</div>
  <div class="card-rule"></div>
  <div class="card-price">$5,00,000+</div>
</div>

<div class="btn btn-small" style="top:2474px;left:550px;width:100px;height:33px">View More</div>

<!-- About -->
<div class="abs about-photo" role="img" aria-label="Contemporary concrete and timber house among trees"></div>
<div class="abs about-panel">
  <h2>Who Is Brindlewood?</h2>
  <p>Brindlewood means "the home, the house", buying a property is one of the most expensive expenses and important assets for people. Brindlewood is a real estate company located in Harlow Park, ACT.</p>
  <p>Being a portfolio sales agent and property manager, coupled with our high-profile international real estate experience, Brindlewood is considered a market leader on the cutting edge with deep industry knowledge, ranging from landlord-tenant relationships, residential purchases.</p>
  <p class="note">FOR CONFIDENTIALITY REASONS,20 TO 30% OF OUR PROPERTIES PLEASE CALL US FOR MORE INFORMATION.</p>
</div>
<div class="btn btn-small" style="top:3303px;left:560px;width:106px;height:33px">More About</div>

<!-- Testimonial -->
<h2 class="section-title" style="top:3450px">What Our People Says</h2>
<svg class="abs" style="top:3518px;left:578px" width="44" height="34" viewBox="0 0 44 34"><path d="M2 32c0-12 4-22 14-28l3 4c-5 4-7 8-7 12h6v12zM24 32c0-12 4-22 14-28l3 4c-5 4-7 8-7 12h6v12z" fill="#e8b14a"/></svg>
<p class="abs quote-text">I would highly recommend Brindlewood Homes property to you, they were helping me manage my investment property, they found a quality tenant in 2 days and maintain my property in a really good condition, they will update everything with me all the time and settle my worries. Tessa, who is my PM, she is very patient and professional. I have had a bad property management experience, hence, I have had lots worries and questions, but Tessa gained my trust and has done a really good job.</p>
<div class="abs quote-name">J. Marlow</div>
<div class="abs arrow-box arrow-fill" style="top:3620px;left:211px;width:37px;height:37px"><svg width="10" height="14"><path d="M8 1L2 7l6 6" fill="none" stroke="#fff" stroke-width="1.6"/></svg></div>
<div class="abs arrow-box arrow-line" style="top:3620px;left:937px;width:37px;height:37px"><svg width="10" height="14"><path d="M2 1l6 6-6 6" fill="none" stroke="#1d2433" stroke-width="1.6"/></svg></div>

<!-- Contact -->
<div class="abs contact"></div>
<h2 class="section-title contact-title" style="top:3910px">Get In Touch With Us</h2>
<p class="abs contact-text">Lorem Ipsum is simply dummy text of the printing and typesetting industry. Lorem Ipsum has been the industry's standard dummy text ever since the 1500.</p>
<div class="abs field" style="top:4048px;left:257px;width:348px">Name</div>
<div class="abs field" style="top:4048px;left:631px;width:354px">Phone No.</div>
<div class="abs field" style="top:4108px;left:257px;width:348px">Email</div>
<div class="abs field" style="top:4108px;left:631px;width:354px;display:flex;justify-content:space-between">Sales<svg width="12" height="8"><path d="M1 1l5 5 5-5" fill="none" stroke="#8fa3c4" stroke-width="1.4"/></svg></div>
<div class="abs field" style="top:4168px;left:257px;width:728px;height:82px">Message</div>
<div class="btn btn-small submit" style="border-bottom:3px solid #c9861a">Request Free Consultation</div>

<!-- Footer -->
<div class="abs brand" style="top:4436px;left:60px;gap:10px">
  <div class="brand-mark" style="width:42px;height:42px"></div>
  <div>
    <div class="brand-name" style="font-size:30px">Brindlewood</div>
    <div class="brand-sub" style="color:var(--orange);font-size:9px">Homes</div>
  </div>
</div>
<p class="abs footer-text" style="top:4500px;left:60px;width:200px">Lorem ipsum dolor sit amet, consectetur adipiscing elit, sed do eiusmod tempor...</p>

<div class="abs footer-head" style="top:4435px;left:332px">Site Map</div>
<div class="abs footer-links" style="top:4464px;left:332px">
  <a>Home</a><a>About Us</a><a>Leasing</a><a>Buy</a><a>Sell</a><a>Our Team</a><a>Blog</a><a>Contact Us</a>
</div>

<div class="abs footer-head" style="top:4435px;left:613px">Contact Us</div>
<svg class="abs" style="top:4474px;left:611px" width="20" height="24" viewBox="0 0 20 24"><path d="M10 22S3 14 3 9a7 7 0 0114 0c0 5-7 13-7 13z" fill="none" stroke="#1d2433" stroke-width="1.3"/><circle cx="10" cy="9" r="2.5" fill="none" stroke="#1d2433" stroke-width="1.3"/></svg>
<p class="abs footer-text" style="top:4470px;left:644px;width:200px;line-height:20px;font-size:12px">18/4 Wattlebird Ave,<br>Harlow Park, ACT, 2900</p>
<svg class="abs" style="top:4522px;left:612px" width="18" height="18" viewBox="0 0 18 18"><path d="M4 1l3 4-2 2c1 2 3 4 5 5l2-2 4 3-2 3C8 16 2 10 1 4z" fill="none" stroke="#1d2433" stroke-width="1.2"/></svg>
<p class="abs footer-text" style="top:4518px;left:647px;font-weight:600;line-height:26px">02 6000 1234<br>02 6000 5678</p>
<svg class="abs" style="top:4574px;left:611px" width="22" height="16" viewBox="0 0 22 16"><rect x="1" y="1" width="20" height="14" fill="none" stroke="#1d2433" stroke-width="1.2"/><path d="M1 1l10 8 10-8" fill="none" stroke="#1d2433" stroke-width="1.2"/></svg>
<p class="abs footer-text" style="top:4571px;left:644px">info@brindlewoodhomes.com.au</p>

<div class="abs footer-head" style="top:4435px;left:888px">Follow On Us</div>
<div class="abs social on" style="top:4472px;left:888px"></div>
<div class="abs social" style="top:4472px;left:943px"></div>
<div class="abs social" style="top:4472px;left:998px"></div>
<div class="abs social" style="top:4472px;left:1051px"></div>

<div class="abs copy-rule"></div>
<div class="abs copy" style="left:60px">2022© Brindlewood Homes. All right reserved.</div>
<div class="abs copy" style="left:655px">Privacy</div>
<div class="abs copy" style="left:724px">Complaint Handling &amp; Dispute Resolution</div>
<div class="abs copy" style="left:998px">Due Diligence Checklist</div>

</body>
</html>
```